Targeted Marketing

Postcard will be sent to customers who’ve already been contacted or will be in the next week or two reiterating information found on my website www.pinevaleminerals.example. Trying to keep my company name in the forefront of their mind when it comes time to divest their mineral interests.

```html
<!DOCTYPE html>
<html lang="en">
<head>
<meta charset="utf-8">
<title>Pinevale Minerals — Postcard</title>
<link rel="stylesheet" href="https://fonts.googleapis.com/css2?family=Open+Sans:wght@400;600;700&family=Roboto+Condensed:ital,wght@1,500&display=swap">
<style>
  :root {
    --red: #ec2027;
    --red-deep: #c81a20;
    --black: #0d0d0d;
    --ink: #141414;
    --white: #ffffff;
    --rule: #f7efe6;
    --sky-top: #a79d9b;
    --sky-warm: #dca88f;
    --ground: #8f8e8c;
  }
  * { margin: 0; padding: 0; box-sizing: border-box; }
  html, body { width: 1200px; height: 816px; overflow: hidden; background: #fff; }
  .postcard {
    position: relative;
    width: 1200px;
    height: 816px;
    overflow: hidden;
    font-family: "Open Sans", Arial, sans-serif;
  }
  .backdrop, .bands { position: absolute; inset: 0; width: 1200px; height: 816px; }
  .scene-photo {
    position: absolute; inset: 0;
    background:
      radial-gradient(ellipse 160px 120px at 475px 600px, rgba(250,214,160,0.55), rgba(250,214,160,0) 70%),
      linear-gradient(180deg, var(--sky-top) 0%, #c4a397 28%, var(--sky-warm) 52%, #c99a86 64%, var(--ground) 76%, var(--ground) 100%);
  }
  .brand {
    position: absolute;
    right: 48px;
    top: 98px;
    display: flex;
    align-items: center;
    gap: 14px;
  }
  .brand-mark { width: 26px; height: 26px; background: var(--red); }
  .brand-name {
    font-weight: 700;
    font-size: 46px;
    line-height: 1;
    color: var(--ink);
    letter-spacing: -0.5px;
  }
  .label {
    position: absolute;
    font-family: "Roboto Condensed", "Arial Narrow", sans-serif;
    font-style: italic;
    font-weight: 500;
    color: var(--white);
    line-height: 1;
    text-transform: uppercase;
  }
  .label .small { font-size: 42px; }
  .label .big { font-size: 58px; }
  .label .under { text-decoration: underline; text-decoration-thickness: 2px; text-underline-offset: 6px; }
  .rule { position: absolute; height: 2px; background: var(--rule); }
  .copy {
    position: absolute;
    right: 48px;
    text-align: right;
    color: var(--ink);
    font-weight: 400;
    font-size: 40px;
    line-height: 43px;
    letter-spacing: 3px;
    white-space: nowrap;
  }
</style>
</head>
<body>
<main class="postcard">
  <div class="scene-photo" role="img" aria-label="Oil pumpjack silhouetted against a hazy sunset over a treeline"></div>

  <svg class="bands" viewBox="0 0 1200 816" aria-hidden="true">
    <defs>
      <linearGradient id="redBand" x1="0" y1="0" x2="1" y2="0">
        <stop offset="0" stop-color="var(--red)"/>
        <stop offset="0.85" stop-color="var(--red)"/>
        <stop offset="1" stop-color="var(--red-deep)"/>
      </linearGradient>
      <linearGradient id="bandShadow" x1="0" y1="0" x2="1" y2="0">
        <stop offset="0" stop-color="#000" stop-opacity="0.35"/>
        <stop offset="1" stop-color="#000" stop-opacity="0"/>
      </linearGradient>
    </defs>
    <polygon points="592,0 612,0 26,816 8,816" fill="url(#bandShadow)"/>
    <polygon points="264,0 592,0 8,816 0,816 0,364" fill="url(#redBand)"/>
    <polygon points="0,0 264,0 0,364" fill="var(--black)"/>
  </svg>

  <div class="brand">
    <span class="brand-mark"></span>
    <span class="brand-name">Pinevale Minerals</span>
  </div>

  <div class="label" style="left:244px; top:187px;"><span class="small">Who</span></div>
  <div class="label" style="left:214px; top:227px;"><span class="small">We </span><span class="big">Are</span></div>
  <div class="rule" style="left:214px; top:277px; width:938px;"></div>
  <p class="copy" style="top:284px;">Experienced, trusted specialists.</p>

  <div class="label" style="left:108px; top:346px;"><span class="small">What</span></div>
  <div class="label" style="left:48px; top:386px;"><span class="small">We </span><span class="big">Offer</span></div>
  <div class="rule" style="left:118px; top:436px; width:1034px;"></div>
  <p class="copy" style="top:442px;">Fair, knowledgeable assistance<br>to clients interested in converting<br>their mineral rights into cash.</p>

  <div class="label" style="left:50px; top:576px;"><span class="big under">We</span></div>
  <div class="rule" style="left:50px; top:627px; width:1100px;"></div>
  <p class="copy" style="top:637px; letter-spacing:4px; right:50px;">know this industry. We can offer you<br>a hassle-free closing process<br>and competitive, fair-market prices.</p>
</main>
</body>
</html>
```